LA's Newest HEMP Facial Oil and Body Oil Packaging Project

We need a packaging concept for a Hemp based facial oil and body oil. We need label design for the bottle and carton graphics. I am attaching a few reference photos. The target demographic is women between 17-35 year old. Products need to be able to stand out in crowded stores with clear calls to action.
1oz Dropper Bottle with Unit Carton - Hemp Facial Oil
4oz PET Bottle with Unit Carton - Hemp + Rose Facial Oil

```html
<!DOCTYPE html>
<html lang="en">
<head>
<meta charset="UTF-8">
<title>Hemp Oil Packaging – Cartons and Labels</title>
<link rel="stylesheet" href="https://fonts.googleapis.com/css2?family=Yellowtail&family=Pinyon+Script&display=swap">
<style>
  :root {
    --page: #ffffff;
    --carton-green: #1d3a1c;
    --carton-green-deep: #142b14;
    --label-green: #2e552c;
    --label-rim: #4d7a45;
    --leaf-tone-soft: rgba(80, 130, 66, 0.45);
    --cap-cream: #f7f0c4;
    --cap-mint: #dcedc0;
    --cap-blush: #f8d6d6;
    --ink-cream: #eef2d6;
    --ink-blush: #f6dcd8;
  }
  html, body {
    margin: 0;
    padding: 0;
    width: 1200px;
    height: 1000px;
    overflow: hidden;
    background: var(--page);
  }
  .canvas {
    position: relative;
    width: 1200px;
    height: 1000px;
    display: flex;
    flex-direction: column;
    align-items: center;
    justify-content: center;
    gap: 50px;
  }
  .carton-row, .label-row {
    display: flex;
    gap: 70px;
  }
  .carton {
    position: relative;
    width: 300px;
    height: 540px;
    background: linear-gradient(180deg, var(--carton-green) 0%, var(--carton-green-deep) 100%);
    overflow: hidden;
  }
  .carton-cap { height: 64px; }
  .carton--tea .carton-cap { background: var(--cap-cream); }
  .carton--facial .carton-cap { background: var(--cap-mint); }
  .carton--rose .carton-cap { background: var(--cap-blush); }

  .leaf-art {
    position: absolute;
    left: 50%;
    transform: translateX(-50%);
    border-radius: 50%;
    background: radial-gradient(ellipse at center, var(--leaf-tone-soft) 0%, rgba(63,107,53,0.15) 55%, rgba(63,107,53,0) 72%);
  }
  .carton .leaf-art {
    top: 150px;
    width: 280px;
    height: 300px;
  }

  .product-name {
    position: absolute;
    left: 0;
    right: 0;
    margin: 0;
    display: flex;
    flex-direction: column;
    align-items: center;
    justify-content: center;
    text-align: center;
    font-family: "Yellowtail", "Brush Script MT", cursive;
    font-weight: 400;
    color: var(--ink-cream);
    line-height: 1;
    white-space: nowrap;
  }
  .carton--rose .product-name,
  .label--rose .product-name { color: var(--ink-blush); }

  .carton .product-name {
    top: 64px;
    bottom: 0;
    font-size: 38px;
  }
  .product-name .joiner {
    font-family: "Pinyon Script", "Brush Script MT", cursive;
    font-size: 0.55em;
    line-height: 1.1;
  }
  .product-name .key {
    font-size: 1.5em;
    line-height: 1;
  }

  .label {
    position: relative;
    width: 230px;
    height: 290px;
    border-radius: 50%;
    background: var(--label-green);
    box-shadow: inset 0 0 0 6px var(--label-green), inset 0 0 0 8px var(--label-rim);
    overflow: hidden;
  }
  .label .leaf-art {
    top: 30px;
    width: 210px;
    height: 230px;
  }
  .label .product-name {
    top: 0;
    bottom: 0;
    font-size: 26px;
  }
</style>
</head>
<body>
<main class="canvas">
  <section class="carton-row">
    <article class="carton carton--tea">
      <div class="carton-cap"></div>
      <div class="leaf-art" role="img" aria-label="Hemp leaf illustration with script flourishes"></div>
      <h2 class="product-name"><span>Body Oil</span><span class="joiner">with</span><span class="key">Hemp</span><span>&amp; Tea Tree</span></h2>
    </article>
    <article class="carton carton--facial">
      <div class="carton-cap"></div>
      <div class="leaf-art" role="img" aria-label="Hemp leaf illustration with script flourishes"></div>
      <h2 class="product-name"><span>Facial Oil</span><span class="joiner">with</span><span class="key">Hemp</span></h2>
    </article>
    <article class="carton carton--rose">
      <div class="carton-cap"></div>
      <div class="leaf-art" role="img" aria-label="Hemp leaf illustration with script flourishes"></div>
      <h2 class="product-name"><span>Body Oil</span><span class="joiner">with</span><span class="key">Hemp</span><span>&amp; Rose</span><span>Petals</span></h2>
    </article>
  </section>

  <section class="label-row">
    <div class="label label--tea">
      <div class="leaf-art" role="img" aria-label="Hemp leaf illustration behind label lettering"></div>
      <p class="product-name"><span>Body Oil</span><span class="joiner">with</span><span class="key">Hemp</span><span>&amp; Tea Tree</span></p>
    </div>
    <div class="label label--facial">
      <div class="leaf-art" role="img" aria-label="Hemp leaf illustration behind label lettering"></div>
      <p class="product-name"><span>Facial Oil</span><span class="joiner">with</span><span class="key">Hemp</span></p>
    </div>
    <div class="label label--rose">
      <div class="leaf-art" role="img" aria-label="Hemp leaf illustration behind label lettering"></div>
      <p class="product-name"><span>Body Oil</span><span class="joiner">with</span><span class="key">Hemp</span><span>&amp; Rose</span><span>Petals</span></p>
    </div>
  </section>
</main>
</body>
</html>
```